Looking for awesome business card design with attached existing logo

We are a water, mold, and fire damage restoration company called "Solvane Crest" Looking for an awesome business card that is edgy yet professional and unique. Show me what you got!

```html
<!DOCTYPE html>
<html lang="en">
<head>
<meta charset="utf-8">
<title>Solvane Crest – Business Card</title>
<link href="https://fonts.googleapis.com/css2?family=Montserrat:wght@400;500;600;700&display=swap" rel="stylesheet">
<style>
  :root {
    --backdrop: #5e4d3b;
    --card-white: #ffffff;
    --teal-dark: #2c4a58;
    --teal-mid: #36596a;
    --teal-light: #4f7f93;
    --gold: #d4961c;
    --ink: #2f2f2f;
    --faint: rgba(212, 150, 28, 0.07);
  }
  * { margin: 0; padding: 0; box-sizing: border-box; }
  html, body {
    width: 900px; height: 1200px; overflow: hidden;
    background: var(--backdrop);
    font-family: "Montserrat", sans-serif;
  }
  .canvas { position: relative; width: 900px; height: 1200px; }

  .card {
    position: absolute; left: 80px; width: 742px; height: 441px;
    border-radius: 30px; overflow: hidden;
  }
  .card-front { top: 131px; background: var(--card-white); }
  .card-back  { top: 638px; }

  .front-watermark {
    position: absolute; right: 20px; top: 40px; width: 260px; height: 380px;
    background: radial-gradient(ellipse at center, var(--faint) 0%, rgba(255,255,255,0) 70%);
  }

  .brand {
    position: absolute; left: 42px; top: 118px;
    display: flex; align-items: center; gap: 12px;
  }
  .brand-dot { width: 22px; height: 22px; border-radius: 50%; background: var(--gold); }
  .brand-name {
    font-weight: 700; font-size: 38px; color: var(--teal-dark); letter-spacing: 0.5px;
  }

  .person { position: absolute; left: 39px; top: 272px; }
  .person-name { font-weight: 600; font-size: 27px; color: var(--gold); line-height: 1.1; }
  .person-role { font-size: 16px; color: var(--ink); margin-top: 3px; }

  .divider {
    position: absolute; left: 37px; top: 337px; width: 675px; height: 2px; background: var(--gold);
  }

  .contacts { position: absolute; left: 37px; top: 350px; list-style: none; }
  .contacts li {
    display: flex; align-items: center; gap: 12px;
    font-size: 16px; color: var(--ink); height: 21px;
  }
  .contacts svg { width: 14px; height: 14px; fill: var(--gold); }

  .address {
    position: absolute; left: 532px; top: 366px;
    font-size: 16px; color: var(--ink); line-height: 20px;
  }

  .back-pattern {
    position: absolute; inset: 0;
    background: linear-gradient(100deg, var(--teal-light) 0%, var(--teal-mid) 45%, var(--teal-dark) 75%);
  }
  .back-brand {
    position: absolute; right: 36px; bottom: 46px;
    font-weight: 700; font-size: 17px; color: var(--gold); text-align: right; line-height: 1.15;
  }
</style>
</head>
<body>
<div class="canvas">

  <section class="card card-front">
    <div class="front-watermark" role="img" aria-label="faint enlarged brand mark decoration"></div>

    <div class="brand">
      <span class="brand-dot"></span>
      <span class="brand-name">Solvane Crest</span>
    </div>

    <div class="person">
      <div class="person-name">Lena Hartwig</div>
      <div class="person-role">Owner</div>
    </div>

    <div class="divider"></div>

    <ul class="contacts">
      <li>
        <svg viewBox="0 0 16 16"><path d="M2 6c0-2 2-3 6-3s6 1 6 3v1h-3V5.5H5V7H2zM4 8h8l1.5 5h-11zM8 9a1.6 1.6 0 1 0 0 3.2A1.6 1.6 0 0 0 8 9z"/></svg>
        +49 404 552 0193
      </li>
      <li>
        <svg viewBox="0 0 16 16"><path d="M1 3h14v1.5L8 9 1 4.5zM1 6.2l7 4.5 7-4.5V13H1z"/></svg>
        info@solvanecrest.com
      </li>
      <li>
        <svg viewBox="0 0 16 16"><path d="M8 1a7 7 0 1 0 0 14A7 7 0 0 0 8 1zm0 1.6c.9 0 1.6 1.1 2 2.9H6c.4-1.8 1.1-2.9 2-2.9zM3 8h2.5c0 .9.1 1.8.3 2.6H3.6A5.4 5.4 0 0 1 3 8zm7.2 2.6c.2-.8.3-1.7.3-2.6H13a5.4 5.4 0 0 1-.6 2.6z"/></svg>
        www.solvanecrest.com
      </li>
    </ul>

    <div class="address">
      Kornblumenweg 42<br>
      22769 Hamburg
    </div>
  </section>

  <section class="card card-back">
    <div class="back-pattern" role="img" aria-label="repeating embossed pattern of the brand icon, fading from light to dark teal"></div>
    <div class="back-brand">Solvane<br>Crest</div>
  </section>

</div>
</body>
</html>
```